8"x5" postcard for Wireless Internet introduction to new mountain town market

I need to market high speed internet to a resort mountain town without doing the obvious laptop on a mountain top thing, so tired. We are going to be competing directly with another provider with same cost, but we will be offering free installation. The area is Aspen Colorado, so the clientele are outdoor types who have suffered for years from being disconnected in their mountain town. We offer fast internet and excellent customer service from people who live in their neck of the woods.

Target Market(s)

23-55 years old, both resort living, families and ski bums

Font styles to use
Sans Serif

Colors

Designer to choose colors to be used in the design.

Requirements
Must have
• Visual appeal and fresh verbiage. We don't mind being a little edgy. We are a young company and we want to appeal to people looking for a provider who gets them. We prefer a clean look.
Nice to have
• Nice to have colors that match our logo
Should not have
• stuffy concepts or verbiage that is too much like a car salesman. We don't want to look like a 'big box' company.

```html
<!DOCTYPE html>
<html lang="en">
<head>
<meta charset="utf-8">
<title>Summit Relay Broadband – Super Fast Wireless Internet</title>
<link rel="stylesheet" href="https://fonts.googleapis.com/css2?family=Exo+2:ital,wght@1,900&family=Didact+Gothic&family=Montserrat:wght@500;600;700;900&display=swap">
<style>
  :root {
    --page-bg: #e6e7ea;
    --ink: #111111;
    --white: #ffffff;
    --sun: #fbe21d;
    --amber: #f9a93b;
    --charcoal: #3e3d40;
    --footer-grey: #f1f1f2;
    --wordmark-grey: #8a8a8c;
    --sky-top: #cfe0f0;
    --sky-mid: #f4f6f8;
    --field-light: #8fbf3e;
    --field-dark: #4d7d1b;
  }
  * { box-sizing: border-box; margin: 0; padding: 0; }
  html, body { width: 1200px; height: 1200px; overflow: hidden; background: var(--page-bg); }
  .canvas { position: relative; width: 1200px; height: 1200px; }
  .flyer {
    position: absolute; left: 244px; top: 30px;
    width: 777px; height: 1243px;
    transform: scale(0.917); transform-origin: 0 0;
    background: var(--white); overflow: hidden;
    box-shadow: 0 12px 30px rgba(0,0,0,0.18);
    font-family: "Montserrat", sans-serif; color: var(--ink);
  }
  .hero-photo {
    position: absolute; left: 0; top: 0; width: 777px; height: 790px;
    background: linear-gradient(180deg, var(--sky-top) 0%, var(--sky-mid) 30%, #eef1f0 45%, #a9c97a 52%, var(--field-light) 62%, var(--field-dark) 100%);
  }
  .hero-shapes { position: absolute; left: 0; top: 0; width: 777px; height: 800px; }
  .headline { position: absolute; font-family: "Exo 2", sans-serif; font-style: italic; font-weight: 900; letter-spacing: 2px; line-height: 1; }
  .headline .ghost { position: absolute; color: rgba(120,120,120,0.18); white-space: nowrap; }
  .headline .word {
    position: relative; white-space: nowrap;
    background: linear-gradient(180deg, var(--sun), var(--amber));
    -webkit-background-clip: text; background-clip: text; color: transparent;
    text-shadow: none; filter: drop-shadow(3px 2px 0 #e8741c);
  }
  .headline-super { left: 145px; top: 60px; font-size: 78px; }
  .headline-super .ghost { left: -50px; top: 10px; }
  .headline-fast { left: 270px; top: 145px; font-size: 94px; }
  .headline-fast .ghost { left: -55px; top: 10px; }
  .subhead { position: absolute; left: 0; width: 777px; top: 248px; text-align: center; font-family: "Didact Gothic", sans-serif; font-size: 37px; }
  .badge {
    position: absolute; border-radius: 50%; border: 8px solid var(--white);
    background: linear-gradient(135deg, var(--sun) 0%, var(--amber) 100%);
    display: flex; flex-direction: column; align-items: center; justify-content: center; text-align: center;
  }
  .badge-service { left: 166px; top: 598px; width: 208px; height: 208px; font-weight: 700; font-size: 17px; line-height: 1.6; }
  .badge-install { left: 348px; top: 540px; width: 258px; height: 258px; }
  .badge-install .big { font-weight: 900; font-size: 54px; line-height: 1; }
  .badge-install .small { font-weight: 900; font-size: 22px; margin-top: 4px; }
  .features { position: absolute; left: 83px; top: 840px; list-style: none; }
  .features li { display: flex; align-items: center; gap: 16px; font-weight: 600; font-size: 22px; height: 41.5px; }
  .features svg { width: 14px; height: 16px; }
  .footer-band { position: absolute; left: 0; top: 1042px; width: 777px; height: 119px; background: var(--footer-grey); }
  .brand { position: absolute; left: 43px; top: 1071px; display: flex; align-items: center; gap: 12px; }
  .brand-dot { width: 56px; height: 56px; border-radius: 50%; background: var(--amber); }
  .brand-name { font-weight: 700; font-size: 25px; line-height: 1.1; color: var(--ink); }
  .cta-shape { position: absolute; left: 365px; top: 1042px; width: 412px; height: 119px; }
  .cta-text { position: absolute; right: 52px; top: 1052px; text-align: right; font-weight: 900; }
  .cta-text .call { font-size: 44px; line-height: 1.1; }
  .cta-text .phone { font-size: 33px; line-height: 1.2; }
  .web { position: absolute; left: 0; width: 777px; top: 1192px; text-align: center; font-size: 21px; font-weight: 500; }
  .web strong { font-weight: 700; }
</style>
</head>
<body>
<div class="canvas">
  <div class="flyer">
    <div class="hero-photo" role="img" aria-label="Photo of a cheetah sprinting across a green field beneath a pale cloudy sky"></div>

    <svg class="hero-shapes" viewBox="0 0 777 800" aria-hidden="true">
      <polygon points="0,540 200,625 0,640" fill="var(--ink)"/>
      <polygon points="0,585 200,625 210,655 0,660" fill="var(--charcoal)"/>
      <polygon points="0,660 210,645 220,690 0,693" fill="var(--sun)"/>
      <polygon points="0,693 220,690 230,722 0,728" fill="var(--amber)"/>
      <polygon points="0,728 240,722 250,750 0,782" fill="var(--ink)"/>
      <polygon points="590,618 777,598 777,604 600,628" fill="var(--sun)"/>
      <polygon points="600,628 777,604 777,606 605,640" fill="var(--ink)"/>
      <polygon points="0,782 777,606 777,800 0,800" fill="var(--white)"/>
    </svg>

    <div class="headline headline-super"><span class="ghost" aria-hidden="true">SUPER</span><span class="word">SUPER</span></div>
    <div class="headline headline-fast"><span class="ghost" aria-hidden="true">FAST</span><span class="word">FAST</span></div>
    <p class="subhead">WIRELESS INTERNET</p>

    <div class="badge badge-service"><span>FAST INTERNET<br>AND EXCELLENT<br>CUSTOMER<br>SERVICE</span></div>
    <div class="badge badge-install"><span class="big">FREE</span><span class="small">INSTALLATION</span></div>

    <ul class="features">
      <li><svg viewBox="0 0 14 16"><polygon points="0,0 14,8 0,16 4,8" fill="var(--ink)"/></svg>High speed connections from 50Mbps to 1Gbps!</li>
      <li><svg viewBox="0 0 14 16"><polygon points="0,0 14,8 0,16 4,8" fill="var(--ink)"/></svg>More coverage than wired services</li>
      <li><svg viewBox="0 0 14 16"><polygon points="0,0 14,8 0,16 4,8" fill="var(--ink)"/></svg>Customizable business contracts</li>
      <li><svg viewBox="0 0 14 16"><polygon points="0,0 14,8 0,16 4,8" fill="var(--ink)"/></svg>We engineer private solutions for you</li>
    </ul>

    <div class="footer-band"></div>
    <div class="brand">
      <span class="brand-dot"></span>
      <span class="brand-name">SUMMIT RELAY<br>BROADBAND</span>
    </div>
    <svg class="cta-shape" viewBox="0 0 412 119" aria-hidden="true">
      <defs>
        <linearGradient id="cta-fill" x1="0" x2="1" y1="0" y2="0">
          <stop offset="0" stop-color="var(--amber)"/>
          <stop offset="1" stop-color="var(--sun)"/>
        </linearGradient>
      </defs>
      <polygon points="0,59.5 58,0 412,0 412,119 58,119" fill="url(#cta-fill)"/>
    </svg>
    <div class="cta-text">
      <div class="call">CALL NOW!</div>
      <div class="phone">1 888 555 0142</div>
    </div>

    <p class="web">VISIT US ONLINE AT <strong>WWW.SUMMITRELAY.NET/PEAK</strong></p>
  </div>
</div>
</body>
</html>
```